A new website for Electrical Contractor Business

We are looking for a unique and new WordPress website design which would include 5 Pages - Home Page, Meet the Team, Our Services, Our Projects and Contact Us page.

The global theme for the website needs to be professional but simple to navigate as we cater for both business and home owner customers.

Our core business service is targeted around lighting from single room decorative to large office so the theme should incorporate this in some way.

The home page should include;
Our business logo, Contact number, Email address, small Image rotation box - Highlighting pervious projectsText box - With welcome message, chirpnet feed news reel/Customer feed back box.

I would also like to see a 2 boxes for the separate customer types we services. Business and Home Owner. each box will have a small image with a small text description with a link to the area of the services page relevant to that customer type.

Meet the team page -This will be introducing potential customers to the team so I would like it to include for each team member. Something like a small image and text area which will introduce an outline of the team members skills and abilities.

Our Services page This page will be outlining the different services on offer to the both customer types business and homeowner. Each service should have an image with text description of the service would good here.

Our projects page-Will include images of pervious projects and work we have completed along with a text area for the project description/ outliner.

Contact Us page - Should include a contact form which should include an option for the customer to quest us to call them back, also a selection box for them to inform us our how they found our details would be good.

Colour - The theme colours can be taken from the logo or feel free to impress with your own imagination.

Remember we are looking for a website that will interest our customers enough to except our services or be drawn further into the website.. So call to action links to other areas of the site/ contact page are welcome

Target Market(s)

Business - Office, warehousing and Large Store - lighting and Power
Home owner lighting and power

Coding

Coded - Design and coding required

Number of Pages Required

5+ page

Font styles to use
Serif
Sans Serif

Colors

Designer to choose colors to be used in the design.

Requirements
Must have
• Logo integrated into the website design - i.e. website colours which allow the logo to blend into the design.
Nice to have
• Custom but professional theme catering to business customers, but also show that we do provide services to home owners too.
Should not have
• Sorry am not interested in one oversized block image on rotation covering half the home page.. Images will be needed but not a single block over sized frame with not text, shape. Please use your imagination when considering this design

```html
<!DOCTYPE html>
<html lang="en">
<head>
<meta charset="utf-8">
<title>Lumenline Electrical</title>
<link rel="stylesheet" href="https://fonts.googleapis.com/css2?family=Poppins:wght@300;400;500;600;700&family=Roboto:wght@400;500;700;900&display=swap">
<style>
:root{
  --orange:#f0682a;
  --orange-dark:#d9561b;
  --navy:#1c2d5e;
  --ink:#2f2f2f;
  --grey-text:#6d6d6d;
  --soft-bg:#f4f4f4;
  --footer:#333333;
  --footer-deep:#262626;
  --white:#ffffff;
}
*{box-sizing:border-box;margin:0;padding:0}
html,body{width:1200px;height:2875px;overflow:hidden}
body{position:relative;font-family:"Poppins",Arial,sans-serif;color:var(--ink);background:var(--white)}
.abs{position:absolute}

/* top bar */
.topbar{left:0;top:0;width:1200px;height:29px;background:#fafafa;border-bottom:1px solid #eee;font-size:10px;color:#777}
.topbar .item{position:absolute;top:8px;display:flex;align-items:center;gap:6px;white-space:nowrap}
.topbar svg{width:10px;height:10px;fill:#999}
.topbar .social{position:absolute;right:155px;top:10px;display:flex;gap:10px}
.topbar .social span{width:8px;height:8px;border-radius:50%;background:#999;display:block}

/* header */
.header{left:0;top:29px;width:1200px;height:82px;background:var(--white)}
.brand{position:absolute;left:161px;top:20px;display:flex;align-items:center;gap:10px}
.brand .dot{width:42px;height:42px;border-radius:50%;background:var(--navy)}
.brand .name{font-size:19px;font-weight:600;color:var(--navy);letter-spacing:.3px}
.nav{position:absolute;top:34px;left:482px;display:flex;font-size:12px;text-transform:uppercase}
.nav a{color:#333;text-decoration:none;width:0;white-space:nowrap}
.nav a.active{color:var(--orange)}

/* hero */
.hero{left:0;top:111px;width:1200px;height:474px;background:linear-gradient(100deg,#cfd6dc 0%,#e6eaee 45%,#b9c6d2 100%)}
.hero .photo{position:absolute;left:560px;top:0;width:400px;height:474px;background:linear-gradient(180deg,#d8dde2,#8a9db8 60%,#3a4f8a)}
.hero .kicker{position:absolute;left:161px;top:181px;font-size:20px;color:#333;font-weight:500}
.hero h1{position:absolute;left:159px;top:204px;font-family:"Roboto",sans-serif;font-size:43px;font-weight:900;color:var(--white);letter-spacing:.3px;white-space:nowrap}
.hero .cta{position:absolute;left:161px;top:258px;width:326px;height:34px;border-radius:17px;background:var(--orange);border:2px solid #f7a47d;color:var(--white);font-size:12px;font-weight:600;display:flex;align-items:center;justify-content:center;gap:18px}

/* about band */
.band{left:0;top:585px;width:1200px;height:415px;background:linear-gradient(90deg,var(--orange-dark),var(--orange) 40%,#f08050)}
.about-card{left:161px;top:554px;width:878px;height:378px;background:var(--white);box-shadow:0 6px 20px rgba(0,0,0,.15)}
.about-card .photo{position:absolute;left:0;top:0;width:420px;height:378px;background:linear-gradient(160deg,#f1f1f1,#d5d8dc 60%,#3a5aa8)}
.about-card .body{position:absolute;left:450px;top:50px;width:400px}
.eyebrow{font-size:10px;letter-spacing:3px;color:var(--orange);font-weight:600}
.about-card h2{font-size:26px;color:var(--navy);font-weight:600;margin-top:2px;white-space:nowrap}
.about-card .rule{width:50px;height:2px;background:var(--navy);margin:8px 0 18px}
.about-card p{font-size:10px;line-height:15.5px;color:#555;margin-bottom:16px}
.btn-outline{display:inline-block;border:2px solid var(--navy);border-radius:18px;padding:7px 22px;font-size:9.5px;font-weight:600;color:var(--navy)}

/* services */
.services{left:0;top:1000px;width:1200px;height:524px}
.section-title{font-family:"Roboto",sans-serif;font-weight:700;font-size:36px;text-align:center;color:#3b3b3b}
.services .section-title{position:absolute;top:58px;width:1200px}
.services .lead{position:absolute;left:160px;top:110px;width:880px;text-align:center;font-size:11px;line-height:18px;color:var(--grey-text)}
.service{position:absolute;top:185px;width:300px;text-align:center}
.service .icon{width:92px;height:92px;border-radius:50%;margin:0 auto;display:flex;align-items:center;justify-content:center}
.service .icon svg{width:42px;height:42px;fill:none;stroke:#fff;stroke-width:2.5}
.service h3{font-size:19px;font-weight:500;margin-top:16px;color:#333}
.service p{font-size:11px;line-height:17px;color:var(--grey-text);margin:6px 20px 18px}
.arrow-box{position:absolute;width:26px;height:26px;border:1px solid #bbb;border-radius:3px;background:#fff;display:flex;align-items:center;justify-content:center}
.arrow-box svg{width:10px;height:10px;fill:none;stroke:#555;stroke-width:2}

/* projects */
.projects-head{left:0;top:1524px;width:1200px;height:109px;background:var(--navy)}
.projects-head .section-title{color:#fff;padding-top:48px}
.tiles{left:0;top:1633px;width:1200px;height:257px;display:flex}
.tile{flex:1;position:relative}
.tile.hover{background:var(--orange)}
.tile.hover::before,.tile.hover::after{content:"";position:absolute;background:rgba(255,255,255,.8);left:50%;top:50%}
.tile.hover::before{width:44px;height:2px;transform:translate(-50%,-50%)}
.tile.hover::after{width:2px;height:44px;transform:translate(-50%,-50%)}

/* team */
.team{left:0;top:1978px;width:1200px;height:376px;background:var(--soft-bg)}
.team h2{position:absolute;left:161px;top:40px;font-family:"Roboto",sans-serif;font-size:33px;font-weight:700;color:#444}
.team .lead{position:absolute;left:161px;top:86px;width:880px;font-size:11px;line-height:18px;color:var(--grey-text)}
.member{position:absolute;top:142px;width:214px;height:234px}
.member .overlay{position:absolute;inset:0;background:rgba(28,45,94,.78);color:#fff;text-align:center;padding-top:74px}
.member .overlay strong{display:block;font-size:16px;font-weight:600}
.member .overlay span{font-size:10px;letter-spacing:1px}
.member .links{display:flex;gap:6px;justify-content:center;margin-top:10px}
.member .links i{width:26px;height:26px;border:1.5px solid #fff;border-radius:50%;display:block}

/* footer */
.footer{left:0;top:2396px;width:1200px;height:434px;background:var(--footer)}
.newsletter{left:161px;top:2398px;width:878px;height:104px;background:var(--orange)}
.newsletter .label{position:absolute;left:62px;top:30px;color:#fff;font-size:13px;font-weight:500;line-height:14px}
.newsletter .label b{display:block;font-family:"Roboto",sans-serif;font-size:27px;font-weight:700;line-height:30px}
.newsletter .field{position:absolute;left:302px;top:33px;width:345px;height:40px;background:#fff;font-size:10px;color:#aaa;padding:14px 22px}
.newsletter .submit{position:absolute;left:654px;top:33px;width:150px;height:40px;background:var(--footer);color:#fff;font-size:13px;display:flex;align-items:center;justify-content:center}
.fcol{position:absolute;top:2548px;color:#ddd}
.fcol .small{font-size:13px;color:#ddd}
.fcol h4{font-family:"Roboto",sans-serif;font-size:27px;font-weight:700;color:#fff;line-height:30px;margin-bottom:8px}
.fcol p{font-size:11px;line-height:20px;color:#cfcfcf}
.fcol .icons{display:flex;gap:6px;margin-top:24px}
.fcol .icons i{width:17px;height:17px;background:#ccc;border-radius:3px;display:block}
.post{display:flex;gap:12px;margin-bottom:14px}
.post .thumb{flex:none;width:52px;height:48px;border-radius:6px;background:linear-gradient(135deg,#7b8da5,#f0a070)}
.post b{display:block;font-size:10.5px;color:#fff;text-decoration:underline}
.post p{font-size:11px;line-height:17px}
.fline{left:0;top:2770px;width:1200px;height:1px;background:#444}
.fnav{left:0;top:2792px;width:1200px;display:flex;justify-content:center;gap:45px;font-size:10px;color:#ccc;text-transform:uppercase}
.copy{left:0;top:2830px;width:1200px;height:45px;background:var(--footer-deep);color:#bbb;font-size:9.5px;text-align:center;padding-top:18px}
</style>
</head>
<body>

<div class="abs topbar">
  <div class="item" style="left:161px"><svg viewBox="0 0 10 10"><path d="M2 0l2 2-1 2 3 3 2-1 2 2-2 2C4 10 0 6 0 2z"/></svg>+27 (0) 11 555 0192</div>
  <div class="item" style="left:326px"><svg viewBox="0 0 10 10"><path d="M0 2h10v6H0z"/></svg>INFO@LUMENLINE.EXAMPLE</div>
  <div class="item" style="left:512px"><svg viewBox="0 0 10 10"><circle cx="5" cy="5" r="5"/></svg>WWW.LUMENLINE.EXAMPLE</div>
  <div class="item" style="left:672px"><svg viewBox="0 0 10 10"><path d="M5 0a3.5 3.5 0 0 1 3.5 3.5C8.5 6 5 10 5 10S1.5 6 1.5 3.5A3.5 3.5 0 0 1 5 0z"/></svg>NORTHVALE / EASTRIDGE / SOUTHPORT REGION</div>
  <div class="social" aria-label="Social links: chirpnet and others"><span></span><span></span><span></span><span></span></div>
</div>

<header class="abs header">
  <div class="brand"><span class="dot"></span><span class="name">LUMENLINE ELECTRICAL</span></div>
  <nav class="nav">
    <a class="active" href="#">Home</a>
    <a style="margin-left:90px" href="#">Meet the Team</a>
    <a style="margin-left:145px" href="#">Our Services</a>
    <a style="margin-left:138px" href="#">Projects</a>
    <a style="margin-left:111px" href="#">Contact Us</a>
  </nav>
</header>

<section class="abs hero">
  <div class="photo" role="img" aria-label="Electrician in hard hat and overalls carrying a coil of cable beside a distribution board"></div>
  <div class="kicker">NEW CONSTRUCTION</div>
  <h1>ELECTRICAL WIRING</h1>
  <div class="cta"><span>CALL FOR SERVICE TODAY!</span><span>+27 (0) 11 555 0192</span></div>
</section>

<div class="abs band" role="img" aria-label="Faded orange backdrop of electricians at work"></div>
<article class="abs about-card">
  <div class="photo" role="img" aria-label="Electrician kneeling to wire a wall socket with tools and cable reel"></div>
  <div class="body">
    <div class="eyebrow">YEARS OF EXPERIENCE</div>
    <h2>LUMENLINE ELECTRICAL</h2>
    <div class="rule"></div>
    <p>Vivamus rutrum euismod tellus at malesuada. Fusce eleifend ligula sit amet fermentum placerat. Donec rutrum justo a fermentum condimentum.</p>
    <p>Cras ultricies commodo nulla, vitae pellentesque nunc mattis eu. Praesent varius, velit nec ullamcorper rhoncus, ante sem semper libero, lacinia pharetra nibh velit sit amet velit. Mauris sit amet felis ut est faucibus elementum. Vivamus rutrum euismod tellus at malesuada. Fusce eleifend ligula sit amet fermentum placerat. Donec rutrum justo a fermentum condimentum.</p>
    <span class="btn-outline">READ MORE</span>
  </div>
</article>

<section class="abs services">
  <h2 class="section-title">OUR SERVICES</h2>
  <p class="lead">Lorem ipsum dolor sit amet, consectetur adipiscing elit. Morbi ultricies posuere commodo. Etiam ut consequat erat. Mauris congue mi nec turpis pretium, in scelerisque dolor placerat. Etiam ac magna id ante semper porta vel vitae mauris. Curabitur eget dolor hendrerit</p>
  <div class="arrow-box" style="left:112px;top:300px"><svg viewBox="0 0 10 10"><path d="M7 1L3 5l4 4"/></svg></div>
  <div class="arrow-box" style="left:1058px;top:300px"><svg viewBox="0 0 10 10"><path d="M3 1l4 4-4 4"/></svg></div>
  <div class="service" style="left:143px">
    <div class="icon" style="background:var(--orange)"><svg viewBox="0 0 40 40"><path d="M12 30l16-16M24 10l6 6M8 34l5-5"/></svg></div>
    <h3>Light Setting</h3>
    <p>Lorem ipsum dolor sit amet, consectetur adipiscing elit. Morbi ultricies posuere commodo. Etiam ut consequat erat. Mauris congue</p>
    <span class="btn-outline">READ MORE</span>
  </div>
  <div class="service" style="left:448px">
    <div class="icon" style="background:var(--navy)"><svg viewBox="0 0 40 40"><rect x="9" y="14" width="22" height="12" rx="2"/><path d="M9 26v4M31 26v4"/></svg></div>
    <h3>Room Decoration</h3>
    <p>Lorem ipsum dolor sit amet, consectetur adipiscing elit. Morbi ultricies posuere commodo. Etiam ut consequat erat. Mauris congue</p>
    <span class="btn-outline">READ MORE</span>
  </div>
  <div class="service" style="left:755px">
    <div class="icon" style="background:#3b3b3b"><svg viewBox="0 0 40 40"><rect x="20" y="10" width="12" height="9"/><path d="M8 24h24M12 24v8M28 24v8"/><circle cx="13" cy="15" r="3"/></svg></div>
    <h3>Large Office Setting</h3>
    <p>Lorem ipsum dolor sit amet, consectetur adipiscing elit. Morbi ultricies posuere commodo. Etiam ut consequat erat. Mauris congue</p>
    <span class="btn-outline">READ MORE</span>
  </div>
</section>

<section class="abs projects-head"><h2 class="section-title">OUR PROJECT</h2></section>
<div class="abs tiles">
  <div class="tile" role="img" aria-label="Electrician working at a control panel" style="background:linear-gradient(135deg,#e7b48e,#8a8f95)"></div>
  <div class="tile" role="img" aria-label="Gloved hands fitting a ceiling light" style="background:linear-gradient(135deg,#dfe4ea,#2b5aa8)"></div>
  <div class="tile" role="img" aria-label="Hands wiring a wall socket" style="background:linear-gradient(135deg,#f2f2f2,#c9b9a7)"></div>
  <div class="tile" role="img" aria-label="Technician testing a high voltage panel" style="background:linear-gradient(135deg,#9aa3a8,#d9c452)"></div>
  <div class="tile hover" role="img" aria-label="Electrician project highlighted in orange"></div>
  <div class="tile" role="img" aria-label="Electricians installing wiring in a white room" style="background:linear-gradient(135deg,#eef1f4,#3556a3)"></div>
</div>
<div class="arrow-box" style="left:569px;top:1915px"><svg viewBox="0 0 10 10"><path d="M7 1L3 5l4 4"/></svg></div>
<div class="arrow-box" style="left:604px;top:1915px;border-color:#ddd"><svg viewBox="0 0 10 10"><path d="M3 1l4 4-4 4"/></svg></div>

<section class="abs team">
  <h2>MEET OUR TEAM</h2>
  <p class="lead">dignissim augue nec, facilisis ex. In hac habitasse platea dictumst. Cras risus erat, dictum a ligula id, volutpat cursus turpis. Suspendisse potenti. Aliquam erat volutpat. Nullam ac mauris purus. Class aptent taciti sociosqu ad litora torquent</p>
  <div class="member" role="img" aria-label="Portrait of a team member" style="left:161px;background:linear-gradient(180deg,#f4f4f4,#c8ccd2)"></div>
  <div class="member" style="left:383px;background:linear-gradient(180deg,#6f7a88,#2f3a4f)" role="img" aria-label="Portrait of Daniel Marsh">
    <div class="overlay"><strong>DANIEL MARSH</strong><span>LOREM IPSUM</span><div class="links"><i></i><i></i><i></i></div></div>
  </div>
  <div class="member" role="img" aria-label="Portrait of a team member in a grey suit" style="left:604px;background:linear-gradient(180deg,#8b8e94,#5a5e66)"></div>
  <div class="member" role="img" aria-label="Portrait of a team member in a suit and tie" style="left:826px;background:linear-gradient(180deg,#d9dade,#4f545e)"></div>
</section>

<footer class="abs footer"></footer>
<div class="abs newsletter">
  <div class="label">SUBSCRIBE OUR<b>NEWSLETTER</b></div>
  <div class="field">ENTER YOUR EMAIL ID</div>
  <div class="submit">SUBSCRIBE</div>
</div>
<div class="fcol" style="left:161px;width:300px">
  <div class="small">ABOUT</div>
  <h4>LUMENLINE</h4>
  <p>Maecenas tristique pharetra ex non ultricies. Proin porta commodo magna in tincidunt Duis eget nibh elit. Pellentesque euismod vitae placerat Nulla dignissim leo urna, ut ultricies ante mattis</p>
  <div class="icons"><i></i><i></i><i></i><i></i><i></i></div>
</div>
<div class="fcol" style="left:514px;width:220px">
  <div class="small">CONTACT</div>
  <h4>DETAILS</h4>
  <p>PO BOX 4821,<br>ASHFORD,<br>CT 06000<br>PHONE: 860-555-0147<br>EMAIL: HELLO@LUMENLINE.EXAMPLE</p>
</div>
<div class="fcol" style="left:760px;width:290px">
  <div class="small">LATEST</div>
  <h4>BLOG</h4>
  <div class="post"><div class="thumb" role="img" aria-label="Blog thumbnail of electrical work"></div><div><b>QUISQUE CONSEQUAT</b><p>euismod vitae placerat Nulla dignissim leo urna, ut ultricies ante mattis</p></div></div>
  <div class="post"><div class="thumb" role="img" aria-label="Blog thumbnail of electrical work"></div><div><b>QUISQUE CONSEQUAT</b><p>euismod vitae placerat Nulla dignissim leo urna, ut ultricies ante mattis</p></div></div>
</div>
<div class="abs fline"></div>
<nav class="abs fnav"><span>Home</span><span>Meet the Team</span><span>Our Services</span><span>Projects</span><span>Contact Us</span></nav>
<div class="abs copy">© 2019 LUMENLINE ELECTRICAL. ALL RIGHTS RESERVED.</div>

</body>
</html>
```